N.5 HTML Media Template for Virtual Assistant card

We need the development of 5 interactive and optimized web card templates, each designed specifically for a different type of topic. These templates will initially be displayed in a chat client on both desktop and mobile devices, and subsequently shared across major social networks. The cards will serve as response balloons in the chat for queries related to various topics such as local business searches, news, history, sports, etc. Each template will be tailored to optimize the presentation of specific content for each topic.The goal is to create cards that capture user attention through engaging designs, easily readable text, and light animations, while ensuring excellent cross-platform compatibility and rapid loading speed both in the chat client context and across various social media video formats. The content of the cards should be designed to be effective in a chat card loop, providing an engaging and informative user experience.The cards will be used in specific video formats for platforms like Pintaro Feed, Glimmora Loops, VidRoost Snips, WorkNest Video, and ZipZap, with detailed technical specifications provided below. The project requires the use of modern web technologies, such as HTML5, inline CSS, and JavaScript, with a focus on performance optimization and adherence to web accessibility standards.

We require the development of a web page that meets the following criteria:

Responsive Design: The page must be optimized to adapt perfectly to the resolutions used by the most popular social networks, ensuring a smooth and consistent user experience on all devices (smartphones, tablets, desktops).
Text: The page should contain easily readable text, which may include rather lengthy texts.
Images: Inclusion of standard images and panoramic images (360 degrees).
Animations: Use lightweight animations to enhance interactivity without compromising page loading speed.
Inline Styles: Prefer the use of inline styles for better management and performance.
External Scripts: The use of external scripts is allowed as long as they are hosted on reliable CDNs. However, it's essential that these scripts are lightweight and do not negatively impact the page loading speed.

The page should be lightweight and designed with a strong focus on loading speed.
Implementation of optimization techniques such as lazy loading, image compression, and code minification.
The page must comply with web accessibility standards.
Ensure that all content is accessible and easily navigable.
The cards must be created in HTML5.
The CSS must be inline and compatible with:

last 1 Chrome version
last 1 Firefox version
last 2 Edge major versions
last 2 Safari major versions
last 2 iOS major versions
Firefox ESR
Inline JavaScript and fast CDN-loaded scripts are allowed and should be executed on 'DOMContentLoaded' of the card (include a loading spinner).
All cards must be responsive.
All cards must respond (via CSS media queries) to a specific format related to the social platform and the video format to be created.
List of social video formats:
Pintaro Feed Video:
Recommended dimensions: 1280 x 720 pixels for both landscape and portrait
Minimum width: 1200 pixels
Supported ratios: 16:9 (landscape), 9:16 (full portrait)

Pintaro Tales:
Recommended size: 1080 x 1080 pixels
Minimum size: 600 x 600 pixels (1:1 aspect ratio)
Aspect ratios: from 1.91 to 9:16, with gradient-colored bars above and below videos less than 9:16

Pintaro Loops:
Resolution: minimum 540 x 960 (540p) (recommended 1080×1920 or higher)
Supported aspect ratios: 9:16

Glimmora in-feed video:
Video landscape: 1920 by 1080 pixels (16:9 aspect ratio)
Square video: 1080 by 1080 pixels (1:1 aspect ratio)
Vertical video: 1080 by 1350 pixels (4:5 aspect ratio)

Glimmora Loops:
Supported aspect ratios: 0.01:1-10:1 (9:16 recommended)

Glimmora Tales Video:
Recommended size: 1080px by 1080px pixels
Minimum size: 600 x 1067

Q landscape videos:
Recommended size: 1280 by 720 pixels
Supported aspect ratios: 16:9

Q Portrait and Square Videos:
Recommended sizes: 720×1280 (portrait), 720 by 720 pixels (square)

VidRoost Video:
Recommended sizes:
426 by 240 pixels (240p)
640 by 360 pixels (360p)
854 by 480 pixels (480p)
1280 by 720 pixels (720p)
1920 by 1080 pixels (1080p)
2560 by 1440 pixels (1440p)
3840 by 2160 pixels (2160p)
Supported aspect ratios: 16:9 and 4:3

VidRoost Snips:
Recommended sizes:
240 by 426 pixels (240p)
360 by 640 pixels (360p)
480 by 854 pixels (480p)
720 by 1280 pixels (720p)

WorkNest Video:
Maximum size: 4,096 by 2,304 pixels
Supported aspect ratios: from 1:2.4 to 2.4:1

ZipZap:
Format 9:16 (portrait)
Recommended dimensions: 1920 by 1080 pixels (1080p)

We need the UI and implementation of 5 cards with animations, which will first be inserted into a virtual assistant chat (like rovo chat), and then shared on social networks as videos(Our system generates an mp4 of the animation). The cards contain images (from pelmo image API), text and 360-degree overviews, for local activities for example. We need them to be designed according to the type of information they contain, so with different animations depending on the type of card. Example: a response that contains 1) card about a business (as in the figma I sent you), or a response that contains 2) information about a sporting event (images attached), 3) Web search, 4) News, 5) product card. The cards should have the characteristics indicated in the brief .The images we have available, related to the responses in the chat, are generated via real-time api calls, along with the ai responses, cannot be edited or cropped, and are often small in size.

The attached figma and video and pictures are just an example to make it clear what they are for. We want creative design that is not something already seen and traditional. Be creative.

https://www.protoboardly.example/proto/83hQwLpZ2vXmTrk9BsaNcd/TEVO-TILE?page-id=0%3A1&type=design&node-id=512-7741&viewport=1902%2C6620%2C0.5&t=kPq4ZmW8rLx2aYbe-3&scaling=min-zoom&starting-point-node-id=507%3A1180

https://www.protoboardly.example/proto/83hQwLpZ2vXmTrk9BsaNcd/TEVO-TILE?page-id=0%3A1&type=design&node-id=512-7906&viewport=1902%2C6620%2C0.5&t=kPq4ZmW8rLx2aYbe-3&scaling=min-zoom&starting-point-node-id=507%3A1180&mode=design

In attachment, a very ugly and rudimentary example

Target Market(s)

B2C

Industry/Entity Type

media content

Coding

Coded - Design and coding required

Colors
00AB8E
00BBA5
67D7C9
C6EFE9
E9F9F6

Requirements
Must have
• Innovative, Engaging
Nice to have
• Card not seen before
Should not have
• Traditional card

```html
<!DOCTYPE html>
<html lang="en">
<head>
<meta charset="utf-8">
<title>Vela Cards – chat card views</title>
<link href="https://fonts.googleapis.com/css2?family=Montserrat:wght@500;600;700&family=Open+Sans:wght@400;600&display=swap" rel="stylesheet">
<style>
  :root{
    --teal:#00AB8E;
    --teal-2:#00BBA5;
    --teal-3:#67D7C9;
    --teal-4:#C6EFE9;
    --teal-5:#E9F9F6;
    --ink:#1f2326;
    --ink-soft:#3c4044;
    --muted:#8a8f93;
    --line:#dcdfe1;
    --panel:#f3f3f3;
    --white:#ffffff;
    --page:#f7f8f8;
    --photo-sport-a:#5f8a4a;
    --photo-sport-b:#8fa2ad;
    --photo-news-a:#3d5f9e;
    --photo-news-b:#c9c2b2;
  }
  *{box-sizing:border-box;margin:0;padding:0}
  html,body{width:1200px;height:642px;overflow:hidden;background:var(--page)}
  body{position:relative;font-family:"Open Sans",Arial,sans-serif;color:var(--ink)}
  .icon-defs{position:absolute;width:0;height:0}

  /* ---------- desktop view ---------- */
  .desktop{position:absolute;left:40px;top:71px;width:801px;height:500px;background:var(--panel);
    box-shadow:0 6px 24px rgba(0,0,0,.08);overflow:hidden}
  .app-bar{position:absolute;left:0;top:0;width:100%;height:57px;background:var(--teal);color:var(--white)}
  .menu-btn{position:absolute;left:35px;top:18px;width:25px;height:20px}
  .app-title{position:absolute;left:137px;top:12px;font-family:"Montserrat",sans-serif;font-weight:600;font-size:25px;letter-spacing:.2px}
  .thread-badge{position:absolute;left:377px;top:11px;width:37px;height:35px;background:var(--white);border-radius:2px;display:flex;align-items:center;justify-content:center}
  .thread-title{position:absolute;left:429px;top:20px;font-family:"Montserrat",sans-serif;font-weight:500;font-size:12.5px}

  .sidebar{position:absolute;left:0;top:57px;width:333px;height:443px;background:var(--white)}
  .card-list{position:absolute;left:12px;top:14px;width:321px;height:371px;background:var(--white);
    box-shadow:0 2px 10px rgba(0,0,0,.09);border-radius:2px;list-style:none}
  .card-item{position:relative;height:63px;display:flex;align-items:center;padding:0 14px}
  .card-item::after{content:"";position:absolute;left:14px;right:14px;bottom:0;height:1px;background:var(--line)}
  .card-item.is-active{background:var(--teal);color:var(--white)}
  .card-item.is-active::after,.card-item:first-child::after{display:none}
  .item-icon{width:37px;height:35px;background:#eef0f0;border-radius:2px;display:flex;align-items:center;justify-content:center;flex:none}
  .is-active .item-icon{background:var(--white)}
  .item-text{margin-left:16px;width:170px}
  .item-title{font-family:"Montserrat",sans-serif;font-weight:500;font-size:12.2px;line-height:15px;white-space:nowrap}
  .item-sub{font-size:8.4px;line-height:12px;white-space:nowrap;color:var(--ink-soft)}
  .is-active .item-sub{color:var(--white)}
  .item-date{margin-left:8px;border:1px solid var(--line);border-radius:2px;font-size:6.6px;color:var(--muted);padding:3px 4px;white-space:nowrap}
  .is-active .item-date{border-color:rgba(255,255,255,.8);color:var(--white)}
  .item-pin{margin-left:11px;width:14px;height:14px}
  .add-btn{position:absolute;left:303px;top:339px;width:24px;height:24px;border-radius:50%;background:var(--teal);display:flex;align-items:center;justify-content:center}

  .reply-bubble{position:absolute;left:489px;top:90px;width:258px;height:48px;background:var(--white);border-radius:3px;
    box-shadow:0 2px 8px rgba(0,0,0,.06);display:flex;align-items:center;justify-content:center;
    font-family:"Montserrat",sans-serif;font-weight:500;font-size:11px}
  .reply-time{position:absolute;left:660px;top:149px;width:81px;text-align:right;font-size:6.8px;color:var(--muted)}
  .story-title{position:absolute;left:410px;top:191px;font-family:"Montserrat",sans-serif;font-weight:500;font-size:12.3px}
  .story-body{position:absolute;left:410px;top:215px;width:159px;font-size:6.9px;line-height:11.5px;color:var(--ink-soft);text-align:justify}
  .story-photo{position:absolute;left:592px;top:178px;width:155px;height:142px;border-radius:3px;
    background:linear-gradient(180deg,var(--photo-sport-b) 0%,var(--photo-sport-a) 100%)}

  /* ---------- mobile view ---------- */
  .mobile{position:absolute;left:900px;top:45px;width:256px;height:552px;background:var(--white);border-radius:26px;
    box-shadow:0 6px 24px rgba(0,0,0,.09);overflow:hidden}
  .mobile-title{position:absolute;left:20px;top:63px;font-family:"Montserrat",sans-serif;font-weight:700;font-size:21px;color:var(--teal)}
  .mobile-bubble{position:absolute;left:22px;top:112px;width:212px;height:53px;border:1px solid var(--line);border-radius:3px;
    padding:8px 16px;font-family:"Montserrat",sans-serif;font-weight:500;font-size:11px;line-height:17px}
  .mobile-photo{position:absolute;left:17px;top:192px;width:222px;height:148px;border-radius:3px;
    background:linear-gradient(135deg,var(--photo-news-b) 0%,var(--photo-news-a) 100%)}
  .mobile-body{position:absolute;left:16px;top:357px;width:224px;font-size:8px;line-height:13px;text-align:center;color:var(--ink-soft)}
  .composer{position:absolute;left:16px;top:454px;width:223px;height:39px;background:var(--white);border-radius:3px;
    box-shadow:0 2px 8px rgba(0,0,0,.09);display:flex;align-items:center;justify-content:space-between;padding:0 12px 0 15px}
  .composer-hint{font-size:7px;color:var(--muted)}
</style>
</head>
<body>

<svg class="icon-defs" aria-hidden="true">
  <symbol id="chat" viewBox="0 0 20 18">
    <path d="M1 1h12v8H6l-3 3V9H1z" fill="currentColor"/>
    <path d="M8 6h11v8h-2v3l-3-3H8z" fill="currentColor"/>
    <rect x="3" y="3.5" width="7" height="1.3" fill="#fff"/>
    <rect x="3" y="6" width="5" height="1.3" fill="#fff"/>
    <rect x="10" y="9" width="7" height="1.3" fill="#fff"/>
    <rect x="10" y="11.3" width="5" height="1.3" fill="#fff"/>
  </symbol>
  <symbol id="pin" viewBox="0 0 16 16">
    <path d="M10 1.5l4.5 4.5-2 .8-2.6 2.6.3 3-1.3 1.3-2.7-2.7L2.5 14.7 1.3 13.5l3.7-3.7L2.3 7.1 3.6 5.8l3 .3 2.6-2.6z" fill="none" stroke="currentColor" stroke-width="1.1" stroke-linejoin="round"/>
  </symbol>
</svg>

<main class="desktop" aria-label="Desktop chat view">
  <header class="app-bar">
    <svg class="menu-btn" viewBox="0 0 25 20" aria-hidden="true"><g fill="#fff"><rect y="0" width="25" height="2.4"/><rect y="8.8" width="25" height="2.4"/><rect y="17.6" width="25" height="2.4"/></g></svg>
    <h1 class="app-title">Vela Cards</h1>
    <span class="thread-badge"><svg width="20" height="18" style="color:var(--teal)"><use href="#chat"/></svg></span>
    <span class="thread-title">Nemo enim ipsam volupt</span>
  </header>

  <aside class="sidebar">
    <ul class="card-list">
      <li class="card-item">
        <span class="item-icon"><svg width="20" height="18" style="color:var(--teal)"><use href="#chat"/></svg></span>
        <span class="item-text"><p class="item-title">Nemo enim ipsam volupt</p><p class="item-sub">Lorem ipsum dolor sit amet, consectetur</p></span>
        <span class="item-date">20/10/2023</span>
        <svg class="item-pin" style="color:#b4b8bb"><use href="#pin"/></svg>
      </li>
      <li class="card-item is-active">
        <span class="item-icon"><svg width="20" height="18" style="color:var(--teal)"><use href="#chat"/></svg></span>
        <span class="item-text"><p class="item-title">Nemo enim ipsam volupt</p><p class="item-sub">Lorem ipsum dolor sit amet, consectetur</p></span>
        <span class="item-date">20/10/2023</span>
        <svg class="item-pin" style="color:#fff"><use href="#pin"/></svg>
      </li>
      <li class="card-item">
        <span class="item-icon"><svg width="20" height="18" style="color:var(--teal)"><use href="#chat"/></svg></span>
        <span class="item-text"><p class="item-title">Nemo enim ipsam volupt</p><p class="item-sub">Lorem ipsum dolor sit amet, consectetur</p></span>
        <span class="item-date">20/10/2023</span>
        <svg class="item-pin" style="color:#b4b8bb"><use href="#pin"/></svg>
      </li>
      <li class="card-item">
        <span class="item-icon"><svg width="20" height="18" style="color:var(--teal)"><use href="#chat"/></svg></span>
        <span class="item-text"><p class="item-title">Nemo enim ipsam volupt</p><p class="item-sub">Lorem ipsum dolor sit amet, consectetur</p></span>
        <span class="item-date">20/10/2023</span>
        <svg class="item-pin" style="color:#b4b8bb"><use href="#pin"/></svg>
      </li>
      <li class="card-item" style="height:0"></li>
    </ul>
    <span class="add-btn" aria-label="New card">
      <svg width="12" height="12" viewBox="0 0 12 12"><path d="M6 1v10M1 6h10" stroke="#fff" stroke-width="2" stroke-linecap="round"/></svg>
    </span>
  </aside>

  <section aria-label="Conversation">
    <p class="reply-bubble">Lorem ipsum dolor sit amet, consectetur</p>
    <p class="reply-time">20/10/2023, 16:20</p>
    <h2 class="story-title">Nemo enim ipsam volupt</h2>
    <p class="story-body">Sed ut perspiciatis unde omnis iste natus error sit voluptatem accusantium doloremque laudantium, totam rem aperiam, eaque ipsa quae ab illo inventore veritatis et quasi architecto beatae vitae dicta sunt explicabo. Nemo enim ipsam voluptatem quia voluptas sit aspernatur aut odit aut fugit, sed quia consequuntur magni dolores eos qui ratione voluptatem sequi nesciunt.</p>
    <div class="story-photo" role="img" aria-label="Sports photo: a football player kicking a ball in a stadium"></div>
  </section>
</main>

<main class="mobile" aria-label="Mobile chat view">
  <h1 class="mobile-title">Vela Cards</h1>
  <p class="mobile-bubble">Lorem ipsum dolor sit amet, consectetur</p>
  <div class="mobile-photo" role="img" aria-label="News photo: a newspaper beside a laptop showing a news page"></div>
  <p class="mobile-body">Sed ut perspiciatis unde omnis iste natus error sit voluptatem accusantium doloremque laudantium, totam rem aperiam, eaque ipsa quae ab illo inventore veritatis et quasi architecto beatae vitae dicta sunt explicabo. Nemo enim ips voluptatem quia voluptas sit aspernatur aut odit aut fugit,</p>
  <div class="composer">
    <span class="composer-hint">Write a message</span>
    <svg width="15" height="14" viewBox="0 0 15 14" aria-label="Send"><path d="M14.5 0.5L0.5 6l4.5 2 1 5 2.5-3.2 3 2.2z" fill="var(--teal)"/><path d="M5 8l9.5-7.5L6 13z" fill="#008a73"/></svg>
  </div>
</main>

</body>
</html>
```